Business Card Design for Event Planning Company

Create a business card for event planning company using our new logo. After I pick the design, I will need files made for 6 employees. Our company provides event design & logistics services as well as venue management. The font should be sans serif and complementary to the logo. I will need to know the name of the font selected for the final design. The phone numbers listed should be separated by "." not "-"

Address for the card
PO Box 318, Washington, DC 20019

Card One
Lorna Pettibone
lpettibone@galavoyant.com
202.481.7730

Card Two
Miriam Okonkwo
mokonkwo@galavoyant.com
202.556.2047

Card Three
Tessa Varnholt
tvarnholt@galavoyant.com
978.620.4471

Card Four
Robin Fess
rfess@galavoyant.com
202.718.3362

Card Five
Ada-Rose Pelletan-Uzor
adarose@galavoyant.com
202.839.1205

Card Six
Beatrix Holloway
Beatrix@galavoyant.com
202.492.6618

Target Market(s)

Corporate/Non-Profit

Industry/Entity Type

Event Planning

Contact Information for Business Card

Address for the card

Card One
Lorna Pettibone
lpettibone@galavoyant.com
202.481.7730

Card Two
Miriam Okonkwo
202.556.2047

Card Three
Tessa Varnholt
978.620.4471

Card Four
Robin Fess
rfess@galavoyant.com
202.718.3362

Card Five
Ada-Rose Pelletan-Uzor
202.839.1205

Card Six
Beatrix Holloway
202.492.6618

Font styles to use
Sans Serif

Colors

Designer to choose colors to be used in the design.

Requirements
Must have
• Two-sided with logo
Should not have
• Extra colors or be too busy

```html
<!DOCTYPE html>
<html lang="en">
<head>
<meta charset="utf-8">
<title>Galavoyant Business Card</title>
<link rel="stylesheet" href="https://fonts.googleapis.com/css2?family=Open+Sans:wght@400;700&display=swap">
<style>
  :root {
    --teal: #4f9c98;
    --ink: #111111;
    --paper: #f6f6f6;
    --text: #2b2b2b;
    --backdrop: #5a5c5e;
    --back-dark: #151515;
    --back-mid: #242424;
  }
  * { box-sizing: border-box; margin: 0; padding: 0; }
  html, body { width: 1200px; height: 904px; overflow: hidden; }
  body {
    background: var(--backdrop);
    font-family: "Open Sans", Arial, sans-serif;
    display: flex; flex-direction: column; align-items: center; justify-content: center;
    gap: 36px;
  }
  .card {
    position: relative;
    width: 700px; height: 400px;
    border-radius: 4px;
    overflow: hidden;
    box-shadow: 0 10px 24px rgba(0,0,0,0.35);
  }
  /* Back side */
  .card-back { background: var(--back-dark); }
  .back-pattern {
    position: absolute; inset: 0;
    background: radial-gradient(circle at 40% 40%, var(--back-mid), var(--back-dark) 75%);
  }
  .back-brand {
    position: absolute; right: 36px; bottom: 150px;
    display: flex; align-items: center; gap: 8px;
    color: #ffffff; font-size: 20px; font-weight: 400; letter-spacing: 0.5px;
  }
  .brand-dot { width: 16px; height: 16px; border-radius: 50%; background: var(--teal); }
  /* Front side */
  .card-front { background: linear-gradient(135deg, #ffffff, var(--paper)); }
  .band-teal {
    position: absolute; left: 0; top: 118px; width: 330px; height: 24px;
    background: var(--teal);
  }
  .band-black {
    position: absolute; left: 370px; right: 0; top: 70px; height: 24px;
    background: var(--ink);
  }
  .front-brand {
    position: absolute; left: 0; right: 0; top: 94px;
    display: flex; align-items: center; justify-content: center; gap: 10px;
    color: var(--text); font-size: 34px; font-weight: 400; letter-spacing: 0.5px;
  }
  .front-brand .brand-dot { width: 22px; height: 22px; }
  .person-name {
    position: absolute; left: 0; right: 0; top: 196px;
    text-align: center; color: var(--teal);
    font-size: 24px; font-weight: 700;
  }
  .contact {
    position: absolute; left: 0; right: 0; top: 262px;
    display: flex; justify-content: center; align-items: stretch;
    color: var(--text); font-size: 16px; line-height: 24px;
  }
  .address { text-align: right; padding-right: 16px; }
  .divider { width: 1.5px; background: var(--text); }
  .reach { padding-left: 16px; }
  .reach-line { display: flex; align-items: center; gap: 8px; }
  .reach-line svg { width: 13px; height: 13px; fill: var(--teal); }
  .foot-stripe {
    position: absolute; left: 0; right: 0; bottom: 0; height: 12px;
    background: var(--teal);
  }
</style>
</head>
<body>
  <section class="card card-back">
    <div class="back-pattern" role="img" aria-label="Repeating tone-on-tone leaf pattern across the dark back of the card"></div>
    <div class="back-brand"><span class="brand-dot"></span>galavoyant</div>
  </section>

  <section class="card card-front">
    <div class="band-teal"></div>
    <div class="band-black"></div>
    <div class="front-brand"><span class="brand-dot"></span>galavoyant</div>
    <h1 class="person-name">Lorna Pettibone</h1>
    <div class="contact">
      <div class="address">
        <p>PO Box 318</p>
        <p>Washington, DC 20019</p>
      </div>
      <div class="divider"></div>
      <div class="reach">
        <p class="reach-line">
          <svg viewBox="0 0 24 24" aria-hidden="true"><path d="M6.6 10.8a15 15 0 0 0 6.6 6.6l2.2-2.2a1 1 0 0 1 1-.25 11.4 11.4 0 0 0 3.6.57 1 1 0 0 1 1 1V20a1 1 0 0 1-1 1A17 17 0 0 1 3 4a1 1 0 0 1 1-1h3.5a1 1 0 0 1 1 1 11.4 11.4 0 0 0 .57 3.6 1 1 0 0 1-.25 1z"/></svg>
          202.481.7730
        </p>
        <p class="reach-line">
          <svg viewBox="0 0 24 24" aria-hidden="true"><path d="M2 5h20v14H2z M4 7v.5l8 5 8-5V7z" fill-rule="evenodd"/></svg>
          lpettibone@galavoyant.com
        </p>
      </div>
    </div>
    <div class="foot-stripe"></div>
  </section>
</body>
</html>
```